App Design for FlavorTrek

We need an app design for a new app called FlavorTrek, which is an app designed to inspire exploration through personalized recipe generation, local restaurant discoveries, and a vibrant community platform. It caters to food enthusiasts looking to explore global cuisines or find the best local dining spots, offering a premium experience with selected features available for free.

-------UPDATED-----
This app will be AI Driven and may not be heavily dependent on media (images,videos) at first, especially for the Recipe generator feature. Our goal is to still have attractive UI. The core functionalities we are looking are the following
1. Recipe Generator: Either user choose a specific cuisine(italian,spanish), or user inputs ingredients and get recipe, or get recipe for different occasions (xmas, thanksgiving ) and get a randomly get recipe to cook, plain simple. We expect the recipes to be displayed in clear and not too generic manner starting with ingredients and expected duration at top and then step by step guide. We also intend to enable premium users to have playful action button or icon to get unlimited recipes generated until they find what they like and also have save for later feature. These premium features should be disabled for free users and prompted to subscribe if they click them with nice popup
2. Restaurant Recommendation - will have selected pictures and will be based on inputs such as zip code and other filters such as cousine types. Premium users can filter by price range, get unlimited recommendation, see actual price range in the recommendation and can save for later where they can find it later. Free users cannot filter by price (disabled) and should see it hidden in the recommendation
3. Meal Planning - will include just simple and random meal plan with just one button or limited interaction for free, users need to subscribe to get features such as customized plan such as considering allergies or diet preferences. Premium users can also get a shopping checklist of ingredients for weekly meal preps and their step by step guide for each meal recipe.
2. Community Sharing: users can view posts and engage with community content
Updates

Hello Designers,

The initial price was not fair for the work. So I have increased it. There will also be $50-100 bonus for those who come up with great designs or for those who incorporate interesting stuff. Thank you! Much appreciated 🙏

Colors
0054AA
0677BA
7BADD7
CADEEF
E8F1F8
0094D4
00A9DD
6FCCEA
C7EBF8
E9F6FB
00AB8E
00BBA5
67D7C9
C6EFE9
E9F9F6
FFC000
F8CF3A
FAE287
FDF2CF
FEFAEE
F0912C
F2A743
F7CA91
FBE8D2
FDF5EE
EE7325
F08F49
F5BC92
FAE3D3
FDF4ED
A7469A
B969AE
D3A5CF
EDDBEB
F8F0F9
6B429C
8869AF
B7A5CE
E3DAEB
F3F0F8

```html
<!DOCTYPE html>
<html lang="en">
<head>
<meta charset="utf-8">
<title>FlavorTrek — App Screens</title>
<link href="https://fonts.googleapis.com/css2?family=Outfit:wght@300;400;500;600&display=swap" rel="stylesheet">
<style>
:root{
  --board:#262626;
  --ink:#1c1c1c;
  --muted:#8a8a8f;
  --line:#e6e6ea;
  --yellow:#FFC000;
  --yellow-soft:#F8CF3A;
  --cream:#FDF2CF;
  --cream-2:#FEFAEE;
  --tile:#f4f4f7;
  --dark-card:#2b2621;
  --white:#ffffff;
}
*{box-sizing:border-box;margin:0;padding:0}
html,body{width:1200px;height:864px;overflow:hidden;background:#fff;font-family:'Outfit',sans-serif;color:var(--ink)}
.stage{position:absolute;left:2px;top:0;width:2268px;height:1640px;transform:scale(0.5268);transform-origin:0 0}
.board{position:absolute;left:32px;top:32px;width:2204px;height:1568px;background:var(--board)}
.screen-title{position:absolute;top:132px;width:302px;text-align:center;color:#fff;font-size:33px;font-weight:400}
.phone{position:absolute;top:254px;width:302px;background:#fff;overflow:hidden}
.a{position:absolute}
.status{left:16px;top:10px;font-size:12px;font-weight:500}
.status-icons{right:16px;top:12px;display:flex;gap:4px;align-items:center}
.hello{left:16px;top:44px;font-size:17px;font-weight:500}
.hello .hat{display:inline-block;width:11px;height:12px;background:var(--yellow-soft);border-radius:3px;margin-left:4px;vertical-align:1px}
.sub{font-size:9.5px;color:var(--muted)}
.avatar{border-radius:50%;background:linear-gradient(135deg,#c9b9a7,#5b4a3d)}
.search{left:16px;top:106px;width:270px;height:42px;border:1px solid var(--line);border-radius:8px;background:#fafafb}
.search .ph{position:absolute;left:32px;top:15px;font-size:9px;color:var(--muted)}
.search svg.lens{position:absolute;left:13px;top:14px}
.filter-btn{position:absolute;right:7px;top:7px;width:27px;height:27px;border-radius:6px;background:var(--yellow-soft);display:flex;align-items:center;justify-content:center}
.h2{font-size:13px;font-weight:500}
.btn-y{background:var(--yellow-soft);border-radius:4px;font-size:9.5px;font-weight:500;display:flex;align-items:center;justify-content:center}
.photo{border-radius:8px}
.promo{background:var(--cream);border-radius:8px}
.promo .t{font-size:12px;font-weight:500}
.promo .s{font-size:9px;color:var(--muted)}
.gen-card{border-radius:8px;text-align:center}
.gen-card .t{font-size:11.5px;font-weight:500;margin-top:20px}
.gen-card .s{font-size:9px;line-height:14px;margin-top:4px;padding:0 14px}
.recipe-card{border-radius:8px;background:linear-gradient(160deg,#c9b38a,#6b6e3a 45%,#2c2a22)}
.recipe-card .name{position:absolute;left:10px;bottom:24px;color:#fff;font-size:10.5px;line-height:11px;font-weight:500}
.recipe-card .cat{position:absolute;left:10px;bottom:12px;color:#ddd;font-size:8px}
.badge{position:absolute;left:10px;top:10px;background:var(--yellow-soft);border-radius:8px;font-size:6.5px;padding:2px 7px}
.gen-item{left:16px;width:270px;height:62px;border:1px solid var(--line);border-radius:6px}
.gen-item .n{position:absolute;left:16px;top:15px;font-size:11px;font-weight:500}
.gen-item .c{position:absolute;left:16px;top:33px;font-size:9px;color:var(--muted)}
.prep{position:absolute;right:7px;top:7px;width:71px;height:46px;background:var(--cream-2);border-radius:4px;text-align:center}
.prep .l{font-size:8.5px;color:var(--muted);margin-top:8px}
.prep .v{font-size:11px;font-weight:600;margin-top:2px}
.cat-tile{top:198px;width:63px;height:86px;border:1px solid var(--line);border-radius:30px;background:#fafafb;text-align:center}
.cat-tile .dish{width:42px;height:42px;border-radius:50%;margin:8px auto 0}
.cat-tile .lb{font-size:9.5px;margin-top:12px}
.rest-card{left:16px;width:270px;height:201px;border-radius:8px;background:var(--dark-card);overflow:hidden}
.rest-card .img{position:absolute;left:0;top:0;width:270px;height:146px}
.rest-card .time{position:absolute;left:16px;top:140px;font-size:8px;color:#fff;display:flex;gap:4px;align-items:center}
.rest-card .n{position:absolute;left:16px;top:158px;font-size:11px;color:#fff;font-weight:500}
.rest-card .c{position:absolute;left:16px;top:177px;font-size:9px;color:#8a7d6d}
.rating{position:absolute;right:14px;top:159px;width:38px;height:22px;background:var(--yellow-soft);border-radius:4px;font-size:9px;display:flex;align-items:center;justify-content:center;font-weight:500}
.bookmark{position:absolute;right:12px;top:12px}
.comm-row{left:16px;width:270px;height:40px}
.comm-row .av{position:absolute;left:0;top:2px;width:36px;height:36px;border-radius:50%}
.comm-row .n{position:absolute;left:46px;top:2px;font-size:11px;font-weight:500}
.comm-row .s{position:absolute;left:46px;top:20px;font-size:8.5px;color:var(--muted)}
.comm-row .join{position:absolute;right:0;top:7px;width:45px;height:26px}
.chip{top:316px;height:28px;border:1px solid var(--line);border-radius:4px;font-size:9.5px;display:flex;align-items:center;justify-content:center}
.post{left:16px;width:270px;height:262px;border:1px solid var(--line);border-radius:8px}
.post .av{position:absolute;left:11px;top:11px;width:34px;height:34px;border-radius:50%}
.post .n{position:absolute;left:56px;top:12px;font-size:11px;font-weight:500}
.post .tm{position:absolute;left:56px;top:31px;font-size:8.5px;color:var(--muted)}
.post .dots{position:absolute;right:12px;top:24px;display:flex;gap:2px}
.post .dots i{width:3px;height:3px;border-radius:50%;background:#b5b5ba}
.post .txt{position:absolute;left:11px;top:54px;width:240px;font-size:11px;line-height:16px}
.post .img{position:absolute;left:11px;top:95px;width:247px;height:138px;border-radius:8px}
.post .acts{position:absolute;left:11px;top:243px;right:11px;font-size:10px;display:flex;gap:14px;align-items:center}
.post .acts span{display:flex;gap:5px;align-items:center}
.post .acts .share{margin-left:auto}
.nav-item{left:15px;display:flex;align-items:center;gap:11px;font-size:12px}
.community-scene{left:0;top:748px;width:302px;height:125px;background:linear-gradient(180deg,#ffffff,#f1f3ee 40%,#e4eadf)}
</style>
</head>
<body>
<div class="stage">
<div class="board"></div>

<div class="screen-title" style="left:143px">Home</div>
<div class="screen-title" style="left:448px">Navigation</div>
<div class="screen-title" style="left:812px">Recipe</div>
<div class="screen-title" style="left:1149px">Restaurant</div>
<div class="screen-title" style="left:1478px">Community</div>
<div class="screen-title" style="left:1815px">Meal</div>

<!-- HOME -->
<section class="phone" style="left:143px;height:873px">
  <div class="a status">9:41</div>
  <div class="a status-icons"><svg width="40" height="8"><rect x="0" y="5" width="2" height="3" fill="#111"/><rect x="3" y="3.5" width="2" height="4.5" fill="#111"/><rect x="6" y="2" width="2" height="6" fill="#111"/><rect x="9" y="0.5" width="2" height="7.5" fill="#111"/><path d="M15 3a7 7 0 0 1 9 0M17 5a4 4 0 0 1 5 0" stroke="#111" stroke-width="1.3" fill="none"/><rect x="28" y="1" width="11" height="6" rx="1.5" fill="#111"/></svg></div>
  <div class="a hello">Hello Mike<span class="hat"></span></div>
  <div class="a sub" style="left:16px;top:69px">What you want to cook today?</div>
  <div class="a avatar" role="img" aria-label="User profile photo" style="left:252px;top:46px;width:33px;height:33px"></div>
  <div class="a search"><svg class="lens" width="12" height="12"><circle cx="5" cy="5" r="4" stroke="#888" fill="none"/><path d="M8 8l3 3" stroke="#888"/></svg><span class="ph">Search recipes, restaurants ...</span><div class="filter-btn"><svg width="12" height="9"><path d="M0 1h12M2 4.5h8M4 8h4" stroke="#111" stroke-width="1.3"/></svg></div></div>
  <div class="a promo" style="left:16px;top:160px;width:270px;height:110px">
    <div class="a t" style="left:22px;top:22px">Start Your 30 Days Free Trail</div>
    <div class="a s" style="left:22px;top:41px">Lorem Ipsum is simply dummy text of</div>
    <div class="a btn-y" style="left:22px;top:63px;width:106px;height:26px">Get Premium Plan</div>
    <div class="a" role="img" aria-label="Illustration of a chef carrying a serving cloche" style="left:190px;top:-6px;width:78px;height:114px;border-radius:40px 40px 8px 8px;background:linear-gradient(180deg,#f8cf3a,#f2c14a 60%,#fdf2cf)"></div>
  </div>
  <div class="a h2" style="left:16px;top:297px">Featured Recipes</div>
  <div class="a gen-card" style="left:16px;top:326px;width:112px;height:142px;background:var(--tile);border:1px solid var(--line)">
    <div class="t">Generate Recipe</div>
    <div class="s" style="color:var(--muted)">Based on the ingredients generate your recipe</div>
    <div class="a" style="left:43px;top:102px;width:26px;height:26px;border-radius:50%;background:var(--yellow-soft);display:flex;align-items:center;justify-content:center"><svg width="10" height="8"><path d="M0 4h9M6 1l3 3-3 3" stroke="#111" fill="none"/></svg></div>
  </div>
  <div class="a recipe-card" role="img" aria-label="Photo of white chicken chili in a bowl" style="left:138px;top:326px;width:114px;height:142px"><span class="badge">Premium</span><span class="name">White<br>Chicken Chili</span><span class="cat">Cuisine category</span></div>
  <div class="a recipe-card" role="img" aria-label="Photo of classic stuffed peppers" style="left:261px;top:326px;width:60px;height:142px;background:linear-gradient(160deg,#d24a2a,#7a2a18 50%,#2c1e16)"><span class="name">Classic<br>Stuffed<br>Pepper</span><span class="cat">Cuisine c</span></div>
  <div class="a h2" style="left:16px;top:494px">Nearby Restaurants</div>
  <div class="a" style="left:16px;top:522px;width:218px;height:61px;border:1px solid var(--line);border-radius:6px">
    <div class="a photo" role="img" aria-label="Photo of a restaurant interior" style="left:5px;top:4px;width:60px;height:52px;background:linear-gradient(135deg,#8a5a32,#3a2618);border-radius:4px"></div>
    <div class="a" style="left:77px;top:15px;font-size:11px;font-weight:500">The Hearthside Table</div>
    <div class="a sub" style="left:77px;top:33px;font-size:9px">30 mins | American Cuisine</div>
  </div>
  <div class="a" style="left:244px;top:522px;width:70px;height:61px;border:1px solid var(--line);border-radius:6px"><div class="a" role="img" aria-label="Photo of a dining room" style="left:5px;top:4px;width:60px;height:52px;background:linear-gradient(135deg,#b34a2a,#3a2618);border-radius:4px"></div></div>
  <div class="a community-scene" role="img" aria-label="Photo of plated dishes and fresh leaves scattered on a white table"></div>
  <div class="a" style="left:0;top:623px;width:302px;text-align:center;font-size:16px;line-height:19px">Get Best Recipe in<br>The Community</div>
  <div class="a sub" style="left:0;top:670px;width:302px;text-align:center;font-size:9px;line-height:14px">Lorem Ipsum is simply dummy text of<br>the printing and typesetting</div>
  <div class="a btn-y" style="left:97px;top:710px;width:107px;height:26px">Go To Community</div>
</section>

<!-- NAVIGATION -->
<section class="phone" style="left:477px;height:654px;background:linear-gradient(180deg,#3a2e18,#1f1a12)">
  <div class="a" style="left:0;top:0;width:273px;height:654px;background:#fff">
    <div class="a avatar" role="img" aria-label="User profile photo" style="left:15px;top:31px;width:33px;height:33px"></div>
    <div class="a" style="left:60px;top:30px;font-size:17px;font-weight:500">Hello Mike<span style="display:inline-block;width:11px;height:12px;background:var(--yellow-soft);border-radius:3px;margin-left:4px;vertical-align:1px"></span></div>
    <div class="a sub" style="left:60px;top:53px;font-size:9px">Lorem Ipsum is simply dummy</div>
    <div class="a" style="left:234px;top:33px;width:22px;height:22px;border-radius:50%;background:#111;display:flex;align-items:center;justify-content:center"><svg width="8" height="8"><path d="M1 1l6 6M7 1l-6 6" stroke="#fff" stroke-width="1.5"/></svg></div>
    <div class="a" style="left:0;top:88px;width:273px;height:1px;background:var(--line)"></div>
    <div class="a nav-item" style="top:118px"><svg width="16" height="16"><path d="M2 7l6-5 6 5v7H2z" stroke="#222" fill="none" stroke-width="1.2"/></svg>Home</div>
    <div class="a nav-item" style="top:159px"><svg width="16" height="16"><rect x="3" y="2" width="10" height="12" rx="2" stroke="#222" fill="none" stroke-width="1.2"/><path d="M6 6h4M6 9h4" stroke="#222"/></svg>Recipe</div>
    <div class="a nav-item" style="top:201px"><svg width="16" height="16"><rect x="2" y="2" width="12" height="12" rx="1.5" stroke="#222" fill="none" stroke-width="1.2"/><path d="M5 6h6M5 9h6M5 12h6" stroke="#222"/></svg>Restaurant</div>
    <div class="a nav-item" style="top:242px"><svg width="16" height="16"><path d="M3 2l10 12M13 2L3 14M3 2c3 0 4 3 4 3" stroke="#222" fill="none" stroke-width="1.2"/></svg>Meal</div>
    <div class="a nav-item" style="top:283px"><svg width="16" height="16"><circle cx="5" cy="4" r="2.3" stroke="#222" fill="none"/><circle cx="11" cy="4" r="2.3" stroke="#222" fill="none"/><circle cx="5" cy="11" r="2.3" stroke="#222" fill="none"/><circle cx="11" cy="11" r="2.3" stroke="#222" fill="none"/></svg>Community</div>
    <div class="a nav-item" style="top:325px"><svg width="16" height="16"><circle cx="8" cy="8" r="6.5" stroke="#222" fill="none" stroke-width="1.2"/><circle cx="8" cy="6.5" r="2.2" stroke="#222" fill="none"/><path d="M4 12.5c2-2.5 6-2.5 8 0" stroke="#222" fill="none"/></svg>Profile</div>
    <div class="a promo" style="left:15px;top:535px;width:243px;height:105px">
      <div class="a t" style="left:17px;top:19px">Start Your 30 Days Free Trail</div>
      <div class="a s" style="left:17px;top:38px">Lorem Ipsum is simply dummy text of</div>
      <div class="a btn-y" style="left:17px;top:60px;width:106px;height:26px">Get Premium Plan</div>
      <div class="a" role="img" aria-label="Illustration of a chef carrying a serving cloche" style="left:175px;top:-12px;width:66px;height:114px;border-radius:40px 40px 8px 8px;background:linear-gradient(180deg,#f8cf3a,#f2c14a 60%,#fdf2cf)"></div>
    </div>
  </div>
</section>

<!-- RECIPE -->
<section class="phone" style="left:812px;height:751px">
  <div class="a status">9:41</div>
  <div class="a status-icons"><svg width="40" height="8"><rect x="0" y="5" width="2" height="3" fill="#111"/><rect x="3" y="3.5" width="2" height="4.5" fill="#111"/><rect x="6" y="2" width="2" height="6" fill="#111"/><rect x="9" y="0.5" width="2" height="7.5" fill="#111"/><path d="M15 3a7 7 0 0 1 9 0M17 5a4 4 0 0 1 5 0" stroke="#111" stroke-width="1.3" fill="none"/><rect x="28" y="1" width="11" height="6" rx="1.5" fill="#111"/></svg></div>
  <div class="a hello">Hello Mike<span class="hat"></span></div>
  <div class="a sub" style="left:16px;top:69px">What you want to cook today?</div>
  <div class="a avatar" role="img" aria-label="User profile photo" style="left:252px;top:46px;width:33px;height:33px"></div>
  <div class="a search"><svg class="lens" width="12" height="12"><circle cx="5" cy="5" r="4" stroke="#888" fill="none"/><path d="M8 8l3 3" stroke="#888"/></svg><span class="ph">Search recipes, restaurants ...</span><div class="filter-btn"><svg width="12" height="9"><path d="M0 1h12M2 4.5h8M4 8h4" stroke="#111" stroke-width="1.3"/></svg></div></div>
  <div class="a h2" style="left:16px;top:174px">Featured Recipes</div>
  <div class="a gen-card" style="left:16px;top:202px;width:112px;height:143px;background:var(--yellow-soft)">
    <div class="t">Generate Recipe</div>
    <div class="s">Based on the ingredients generate your recipe</div>
    <div class="a" style="left:43px;top:102px;width:27px;height:27px;border-radius:50%;background:#111;display:flex;align-items:center;justify-content:center"><svg width="10" height="8"><path d="M0 4h9M6 1l3 3-3 3" stroke="#fff" fill="none"/></svg></div>
  </div>
  <div class="a recipe-card" role="img" aria-label="Photo of white chicken chili in a bowl" style="left:138px;top:202px;width:114px;height:143px"><span class="badge">Premium</span><span class="name">White<br>Chicken Chili</span><span class="cat">Cuisine category</span></div>
  <div class="a recipe-card" role="img" aria-label="Photo of classic stuffed peppers" style="left:261px;top:202px;width:60px;height:143px;background:linear-gradient(160deg,#d24a2a,#7a2a18 50%,#2c1e16)"><span class="name">Classic<br>Stuffed<br>Pepper</span><span class="cat">Cuisine c</span></div>
  <div class="a h2" style="left:16px;top:370px">My Generated Recipe</div>
  <div class="a gen-item" style="top:398px"><span class="n">Pizza Casserole</span><span class="c">Cuisine category</span><div class="prep"><div class="l">Prep Time</div><div class="v">24 Min</div></div></div>
  <div class="a gen-item" style="top:466px"><span class="n">Green Chile Chicken Skillet ...</span><span class="c">Cuisine category</span><div class="prep"><div class="l">Prep Time</div><div class="v">24 Min</div></div></div>
  <div class="a gen-item" style="top:535px"><span class="n">Chicken Tamale Pie</span><span class="c">Cuisine category</span><div class="prep"><div class="l">Prep Time</div><div class="v">24 Min</div></div></div>
  <div class="a gen-item" style="top:603px"><span class="n">Taco Spaghetti</span><span class="c">Cuisine category</span><div class="prep"><div class="l">Prep Time</div><div class="v">24 Min</div></div></div>
  <div class="a gen-item" style="top:672px"><span class="n">Pizza Casserole</span><span class="c">Cuisine category</span><div class="prep"><div class="l">Prep Time</div><div class="v">24 Min</div></div></div>
</section>

<!-- RESTAURANT -->
<section class="phone" style="left:1154px;height:1191px">
  <div class="a status">9:41</div>
  <div class="a status-icons"><svg width="40" height="8"><rect x="0" y="5" width="2" height="3" fill="#111"/><rect x="3" y="3.5" width="2" height="4.5" fill="#111"/><rect x="6" y="2" width="2" height="6" fill="#111"/><rect x="9" y="0.5" width="2" height="7.5" fill="#111"/><path d="M15 3a7 7 0 0 1 9 0M17 5a4 4 0 0 1 5 0" stroke="#111" stroke-width="1.3" fill="none"/><rect x="28" y="1" width="11" height="6" rx="1.5" fill="#111"/></svg></div>
  <div class="a hello">Hello Mike<span class="hat"></span></div>
  <div class="a sub" style="left:16px;top:69px">What you want to cook today?</div>
  <div class="a avatar" role="img" aria-label="User profile photo" style="left:252px;top:46px;width:33px;height:33px"></div>
  <div class="a search"><svg class="lens" width="12" height="12"><circle cx="5" cy="5" r="4" stroke="#888" fill="none"/><path d="M8 8l3 3" stroke="#888"/></svg><span class="ph">Search recipes, restaurants ...</span><div class="filter-btn"><svg width="12" height="9"><path d="M0 1h12M2 4.5h8M4 8h4" stroke="#111" stroke-width="1.3"/></svg></div></div>
  <div class="a h2" style="left:16px;top:174px">Categories</div>
  <div class="a cat-tile" style="left:16px"><div class="dish" role="img" aria-label="Burger" style="background:radial-gradient(#8a4a1a,#d8a050 70%)"></div><div class="lb">Burger</div></div>
  <div class="a cat-tile" style="left:87px"><div class="dish" role="img" aria-label="Pizza" style="background:radial-gradient(#e0603a,#e8b060 70%)"></div><div class="lb">Pizza</div></div>
  <div class="a cat-tile" style="left:158px"><div class="dish" role="img" aria-label="Vegetable curry" style="background:radial-gradient(#e8902a,#c04a1a 70%)"></div><div class="lb">Veg</div></div>
  <div class="a cat-tile" style="left:229px"><div class="dish" role="img" aria-label="Roast chicken" style="background:radial-gradient(#a0501a,#4a2a10 70%)"></div><div class="lb">Non-Veg</div></div>
  <div class="a h2" style="left:16px;top:310px">Featured Restaurants</div>

  <div class="a rest-card" style="top:340px"><div class="img" role="img" aria-label="Photo of a table full of dishes" style="background:linear-gradient(160deg,#6a3a1a,#c47a3a 50%,#3a2012)"></div><svg class="bookmark" width="12" height="14"><path d="M1 1h10v12L6 9.5 1 13z" stroke="#fff" fill="none"/></svg><span class="time"><svg width="9" height="9"><circle cx="4.5" cy="4.5" r="3.8" stroke="#fff" fill="none"/><path d="M4.5 2.5v2h1.5" stroke="#fff" fill="none"/></svg>30 min</span><span class="n">The Hearthside Table</span><span class="c">Burger | American Cuisine</span><span class="rating">4.1 ★</span></div>
  <div class="a rest-card" style="top:551px"><div class="img" role="img" aria-label="Photo of grilled steak on a board" style="background:linear-gradient(160deg,#1e1a16,#5a2a1a 55%,#2a1e16)"></div><svg class="bookmark" width="12" height="14"><path d="M1 1h10v12L6 9.5 1 13z" stroke="#fff" fill="none"/></svg><span class="time"><svg width="9" height="9"><circle cx="4.5" cy="4.5" r="3.8" stroke="#fff" fill="none"/><path d="M4.5 2.5v2h1.5" stroke="#fff" fill="none"/></svg>30 min</span><span class="n">The Hearthside Table</span><span class="c">Burger | American Cuisine</span><span class="rating">4.1 ★</span></div>
  <div class="a rest-card" style="top:762px"><div class="img" role="img" aria-label="Photo of a banquet hall with purple lighting" style="background:linear-gradient(160deg,#3a2a8a,#8a3ac0 50%,#2a1a4a)"></div><svg class="bookmark" width="12" height="14"><path d="M1 1h10v12L6 9.5 1 13z" stroke="#fff" fill="none"/></svg><span class="time"><svg width="9" height="9"><circle cx="4.5" cy="4.5" r="3.8" stroke="#fff" fill="none"/><path d="M4.5 2.5v2h1.5" stroke="#fff" fill="none"/></svg>30 min</span><span class="n">The Hearthside Table</span><span class="c">Burger | American Cuisine</span><span class="rating">4.1 ★</span></div>
  <div class="a rest-card" style="top:974px"><div class="img" role="img" aria-label="Photo of a cook plating food in a kitchen" style="background:linear-gradient(160deg,#2a3a4a,#c48a4a 55%,#3a2a1a)"></div><svg class="bookmark" width="12" height="14"><path d="M1 1h10v12L6 9.5 1 13z" stroke="#fff" fill="none"/></svg><span class="time"><svg width="9" height="9"><circle cx="4.5" cy="4.5" r="3.8" stroke="#fff" fill="none"/><path d="M4.5 2.5v2h1.5" stroke="#fff" fill="none"/></svg>30 min</span><span class="n">The Hearthside Table</span><span class="c">Burger | American Cuisine</span><span class="rating">4.1 ★</span></div>
</section>

<!-- COMMUNITY -->
<section class="phone" style="left:1489px;height:1224px">
  <div class="a status">9:41</div>
  <div class="a status-icons"><svg width="40" height="8"><rect x="0" y="5" width="2" height="3" fill="#111"/><rect x="3" y="3.5" width="2" height="4.5" fill="#111"/><rect x="6" y="2" width="2" height="6" fill="#111"/><rect x="9" y="0.5" width="2" height="7.5" fill="#111"/><path d="M15 3a7 7 0 0 1 9 0M17 5a4 4 0 0 1 5 0" stroke="#111" stroke-width="1.3" fill="none"/><rect x="28" y="1" width="11" height="6" rx="1.5" fill="#111"/></svg></div>
  <div class="a hello">Hello Mike<span class="hat"></span></div>
  <div class="a sub" style="left:16px;top:69px">What you want to cook today?</div>
  <div class="a avatar" role="img" aria-label="User profile photo" style="left:252px;top:46px;width:33px;height:33px"></div>
  <div class="a h2" style="left:16px;top:105px">Recommended Community</div>
  <div class="a comm-row" style="top:133px"><div class="av" role="img" aria-label="Community food photo" style="background:radial-gradient(#e0602a,#4a2a1a)"></div><span class="n">Food plazza</span><span class="s">156k people joined</span><div class="join btn-y">Join</div></div>
  <div class="a comm-row" style="top:180px"><div class="av" role="img" aria-label="Community food photo" style="background:radial-gradient(#e8a060,#8a4a2a)"></div><span class="n">Food Lover Community</span><span class="s">156k people joined</span><div class="join btn-y">Join</div></div>
  <div class="a comm-row" style="top:227px"><div class="av" role="img" aria-label="Community food photo" style="background:radial-gradient(#c07a2a,#2a1a10)"></div><span class="n">Roosted Chicken</span><span class="s">156k people joined</span><div class="join btn-y">Join</div></div>
  <div class="a h2" style="left:16px;top:288px">Community Feed</div>
  <div class="a chip" style="left:16px;width:50px;background:#111;color:#fff;border-color:#111;gap:5px"><svg width="10" height="8"><path d="M0 1h10M2 4h6M3.5 7h3" stroke="#fff"/></svg>Filter</div>
  <div class="a chip" style="left:86px;width:64px;border-color:var(--yellow-soft)">Non-Veg</div>
  <div class="a chip" style="left:158px;width:62px">Pizza</div>
  <div class="a chip" style="left:228px;width:62px">Burger</div>
  <div class="a chip" style="left:297px;width:30px"></div>

  <div class="a post" style="top:358px"><div class="av avatar" role="img" aria-label="Author photo"></div><span class="n">Jonah Reeves</span><span class="tm">1h ago</span><div class="dots"><i></i><i></i><i></i></div><p class="txt">Lorem Ipsum is simply dummy text of the printing and typesetting industry.</p><div class="img" role="img" aria-label="Photo of a stir fry in a wok" style="background:linear-gradient(160deg,#1a1a1a,#c0602a 55%,#2a1a12)"></div><div class="acts"><span><svg width="13" height="12"><path d="M1 5h2.5v6H1zM3.5 5l3-4c1 0 1.5.6 1.3 1.6L7.4 4.5H11c.8 0 1.3.7 1.1 1.4l-1 4.2c-.2.6-.7.9-1.2.9H3.5" stroke="#333" fill="none"/></svg>24</span><span><svg width="13" height="12"><path d="M1 1h11v8H5l-3 2.5V9H1z" stroke="#333" fill="none"/><path d="M3.5 4h6M3.5 6h4" stroke="#333"/></svg>5</span></div></div>
  <div class="a btn-y" style="left:170px;top:607px;width:116px;height:45px;border-radius:23px;justify-content:flex-start;padding-left:14px;box-shadow:0 4px 12px rgba(0,0,0,.12)">Create Post<div class="a" style="right:8px;top:8px;width:29px;height:29px;border-radius:50%;background:#fff;display:flex;align-items:center;justify-content:center"><svg width="10" height="10"><path d="M5 0v10M0 5h10" stroke="#111" stroke-width="1.6"/></svg></div></div>

  <div class="a post" style="top:646px"><div class="av avatar" role="img" aria-label="Author photo"></div><span class="n">Miles Harlan</span><span class="tm">1h ago</span><div class="dots"><i></i><i></i><i></i></div><p class="txt">Lorem Ipsum is simply dummy text of the printing and typesetting industry.</p><div class="img" role="img" aria-label="Photo of penne pasta in tomato sauce" style="background:linear-gradient(135deg,#6a4a2a,#e0702a 55%,#4a2a1a)"></div><div class="acts"><span><svg width="13" height="12"><path d="M1 5h2.5v6H1zM3.5 5l3-4c1 0 1.5.6 1.3 1.6L7.4 4.5H11c.8 0 1.3.7 1.1 1.4l-1 4.2c-.2.6-.7.9-1.2.9H3.5" stroke="#333" fill="none"/></svg>24</span><span><svg width="13" height="12"><path d="M1 1h11v8H5l-3 2.5V9H1z" stroke="#333" fill="none"/><path d="M3.5 4h6M3.5 6h4" stroke="#333"/></svg>5</span><span class="share"><svg width="12" height="12"><circle cx="2.5" cy="6" r="2" stroke="#333" fill="none"/><circle cx="9.5" cy="2.5" r="2" stroke="#333" fill="none"/><circle cx="9.5" cy="9.5" r="2" stroke="#333" fill="none"/><path d="M4.3 5l3.4-1.6M4.3 7l3.4 1.6" stroke="#333"/></svg>2</span></div></div>

  <div class="a post" style="top:934px"><div class="av avatar" role="img" aria-label="Author photo"></div><span class="n">Eli Navarro</span><span class="tm">1h ago</span><div class="dots"><i></i><i></i><i></i></div><p class="txt">Lorem Ipsum is simply dummy text of the printing and typesetting industry.</p><div class="img" role="img" aria-label="Photo of lentil soup with spices" style="background:linear-gradient(135deg,#1e2230,#e08a2a 55%,#1e2230)"></div><div class="acts"><span><svg width="13" height="12"><path d="M1 5h2.5v6H1zM3.5 5l3-4c1 0 1.5.6 1.3 1.6L7.4 4.5H11c.8 0 1.3.7 1.1 1.4l-1 4.2c-.2.6-.7.9-1.2.9H3.5" stroke="#333" fill="none"/></svg>24</span><span><svg width="13" height="12"><path d="M1 1h11v8H5l-3 2.5V9H1z" stroke="#333" fill="none"/><path d="M3.5 4h6M3.5 6h4" stroke="#333"/></svg>5</span><span class="share"><svg width="12" height="12"><circle cx="2.5" cy="6" r="2" stroke="#333" fill="none"/><circle cx="9.5" cy="2.5" r="2" stroke="#333" fill="none"/><circle cx="9.5" cy="9.5" r="2" stroke="#333" fill="none"/><path d="M4.3 5l3.4-1.6M4.3 7l3.4 1.6" stroke="#333"/></svg>2</span></div></div>
</section>

<!-- MEAL -->
<section class="phone" style="left:1823px;height:751px">
  <div class="a status">9:41</div>
  <div class="a status-icons"><svg width="40" height="8"><rect x="0" y="5" width="2" height="3" fill="#111"/><rect x="3" y="3.5" width="2" height="4.5" fill="#111"/><rect x="6" y="2" width="2" height="6" fill="#111"/><rect x="9" y="0.5" width="2" height="7.5" fill="#111"/><path d="M15 3a7 7 0 0 1 9 0M17 5a4 4 0 0 1 5 0" stroke="#111" stroke-width="1.3" fill="none"/><rect x="28" y="1" width="11" height="6" rx="1.5" fill="#111"/></svg></div>
  <div class="a hello">Hello Mike<span class="hat"></span></div>
  <div class="a sub" style="left:16px;top:69px">What you want to cook today?</div>
  <div class="a avatar" role="img" aria-label="User profile photo" style="left:252px;top:46px;width:33px;height:33px"></div>
  <div class="a" style="left:16px;top:106px;width:270px;height:151px;background:var(--yellow-soft);border-radius:8px;overflow:hidden">
    <div class="a" style="left:22px;top:20px;font-size:18px;line-height:20px;font-weight:500">Create Your<br>Meal Plan</div>
    <div class="a" style="left:22px;top:67px;font-size:8.5px;line-height:13px">DIscover an unique meal<br>plan using AI</div>
    <div class="a" style="left:22px;top:106px;width:78px;height:26px;background:#111;color:#fff;border-radius:4px;font-size:9px;display:flex;align-items:center;justify-content:center">Create Plan</div>
    <div class="a" role="img" aria-label="Photo of meal prep containers with vegetables and juice" style="left:150px;top:0;width:120px;height:151px;background:linear-gradient(160deg,#e8e4dc,#9ab04a 45%,#e8903a 80%,#f8cf3a)"></div>
  </div>
  <div class="a h2" style="left:16px;top:282px">Today Meal Plan</div>
  <div class="a sub" style="left:16px;top:304px;font-size:9px">You don 't have any meal plan for today</div>
  <div class="a" style="left:16px;top:343px;width:270px;height:258px;background:#fafafc;border:1px solid var(--line);border-radius:8px;text-align:center">
    <div class="a" style="left:110px;top:24px;width:50px;height:50px;border-radius:50%;background:#eceef6;display:flex;align-items:center;justify-content:center"><svg width="14" height="14"><rect x="1.5" y="6" width="11" height="7.5" rx="1.5" fill="#111"/><path d="M4 6V4a3 3 0 0 1 6 0v2" stroke="#111" fill="none" stroke-width="1.4"/><circle cx="7" cy="9.7" r="1.2" fill="#fff"/></svg></div>
    <div class="a" style="left:0;top:90px;width:270px;font-size:16px;font-weight:500">Unlock Your Meal Plan Today</div>
    <div class="a sub" style="left:0;top:118px;width:270px;font-size:9px;line-height:14px">Make your meal plan and maintain your<br>diet everyday</div>
    <div class="a" style="left:0;top:156px;width:270px;font-size:27px;font-weight:500">$12<span style="font-size:12px;font-weight:400">/ month</span></div>
    <div class="a btn-y" style="left:54px;top:208px;width:163px;height:27px;font-size:9px">Subscribe Now&nbsp;<span style="font-weight:400">(50% Discount)</span></div>
  </div>
</section>
</div>
</body>
</html>
```